Amber Hollow Productions

I need a business card design for a new freelance film production company using or incorporating the logo:
I want the card to be creative, minimal, yet professional. Feel free to use a variety of different shapes and sizes/ textures for the card.

Industry/Entity Type

Film Production

```html
<!DOCTYPE html>
<html lang="en">
<head>
<meta charset="utf-8">
<title>Amber Hollow Productions – Business Card</title>
<link rel="stylesheet" href="https://fonts.googleapis.com/css2?family=Josefin+Sans:wght@300;400&family=Tinos&display=swap">
<style>
  :root {
    --film-blue: #3e57aa;
    --hole-white: #f4f7fb;
    --ink-blue: #1f55a1;
    --ink-grey: #4a4a4a;
    --card-white: #ffffff;
    --card-mist: #dfe5ec;
    --page: #ffffff;
  }
  * { box-sizing: border-box; margin: 0; padding: 0; }
  html, body {
    width: 1200px;
    height: 900px;
    overflow: hidden;
    background: var(--page);
  }
  .canvas {
    position: relative;
    width: 1200px;
    height: 900px;
    display: flex;
    align-items: center;
    justify-content: center;
    gap: 60px;
  }
  .card {
    position: relative;
    width: 525px;
    height: 300px;
    overflow: hidden;
    box-shadow: 0 6px 24px rgba(0, 0, 0, 0.12);
  }
  .film-band {
    position: absolute;
    left: 0;
    width: 100%;
    display: block;
  }

  /* Front */
  .card-front {
    background: linear-gradient(170deg, var(--card-white) 35%, var(--card-mist) 100%);
  }
  .card-front .film-band { top: 0; height: 52px; }
  .front-identity {
    position: absolute;
    left: 0;
    right: 0;
    top: 52px;
    bottom: 0;
    display: flex;
    flex-direction: column;
    align-items: center;
    justify-content: center;
    gap: 18px;
  }
  .identity-square {
    width: 46px;
    height: 46px;
    background: var(--film-blue);
  }
  .identity-name {
    font-family: "Josefin Sans", sans-serif;
    font-weight: 400;
    font-size: 30px;
    line-height: 1.2;
    letter-spacing: 0.08em;
    text-transform: uppercase;
    text-align: center;
    color: var(--film-blue);
  }

  /* Back */
  .card-back { background: var(--film-blue); }
  .card-back .band-top { top: 0; height: 44px; }
  .card-back .band-bottom { bottom: 0; height: 44px; }
  .info-panel {
    position: absolute;
    left: 26px;
    right: 26px;
    top: 46px;
    bottom: 46px;
    background: var(--card-white);
    border-radius: 18px;
    display: flex;
    flex-direction: column;
    align-items: center;
    padding-top: 26px;
  }
  .company-name {
    font-family: "Josefin Sans", sans-serif;
    font-weight: 400;
    font-size: 34px;
    line-height: 1.1;
    letter-spacing: 0.04em;
    text-transform: uppercase;
    text-align: center;
    color: var(--ink-blue);
  }
  .contact-lines {
    margin-top: 24px;
    font-family: "Tinos", serif;
    font-size: 21px;
    line-height: 1.2;
    text-align: center;
    color: var(--ink-blue);
    list-style: none;
  }
</style>
</head>
<body>
<main class="canvas">

  <section class="card card-front" aria-label="Business card front">
    <svg class="film-band" viewBox="0 0 525 52" preserveAspectRatio="none" aria-hidden="true">
      <defs>
        <pattern id="front-holes" x="14" y="0" width="47.5" height="52" patternUnits="userSpaceOnUse">
          <rect x="0" y="12" width="23" height="30" rx="5" fill="var(--hole-white)"/>
        </pattern>
      </defs>
      <rect width="525" height="52" fill="var(--film-blue)"/>
      <rect width="525" height="52" fill="url(#front-holes)"/>
    </svg>
    <div class="front-identity">
      <span class="identity-square"></span>
      <p class="identity-name">Amber Hollow<br>Productions</p>
    </div>
  </section>

  <section class="card card-back" aria-label="Business card back">
    <svg class="film-band band-top" viewBox="0 0 525 44" preserveAspectRatio="none" aria-hidden="true">
      <defs>
        <pattern id="back-holes" x="26" y="0" width="50" height="44" patternUnits="userSpaceOnUse">
          <rect x="0" y="8" width="22" height="28" rx="5" fill="var(--hole-white)"/>
        </pattern>
      </defs>
      <rect width="525" height="44" fill="url(#back-holes)"/>
    </svg>
    <div class="info-panel">
      <h1 class="company-name">Amber Hollow<br>Productions</h1>
      <ul class="contact-lines">
        <li>Your Name</li>
        <li>Title</li>
        <li>Phone</li>
      </ul>
    </div>
    <svg class="film-band band-bottom" viewBox="0 0 525 44" preserveAspectRatio="none" aria-hidden="true">
      <rect width="525" height="44" fill="url(#back-holes)"/>
    </svg>
  </section>

</main>
</body>
</html>
```